TORVO BEARD BALM LABEL DESIGN

We need a label design for our new company Torvo beard balm. Our company used to be called Wandering Fern but we changed our name. We currently already have the logo with the old name, so it would be awesome if we can change the name to " Mr. Torvo" in cursive writing.
Rounded Top Circular Tin
60 mm X 20 mm
As for the label, I want it to say " Mr. Torvo Premium Beard Balm" and the words under the Man in suit. I would like the word "Mr. Torvo" to be in a cursive and go from shoulder to shoulder under the man in suit logo in replace of the previous name shown. I would also like the word "Premium Beard Balm" to be under the word " Mr. Torvo" in a smaller, NON-CURSIVE but very sleek font. All of this should be around the middle of the circular label.
The following words can be placed anywhere on the label where it's best suited with any nice looking, smaller font.
- All Natural Oils
- Fresh Cucumber and Black Licorice (Flavor of the balm)
- Aphrodisiac Scent
- 2 oz.
And lastly, I want the color of the label to have a BLACK background and all the words including the Man in suit logo, to be in SILVER. This is a must.
Thank you very much for viewing my description and hopefully you will take my project.
Cheers, Oswin.
Men with Beards
It Company

```html
<!DOCTYPE html>
<html lang="en">
<head>
<meta charset="utf-8">
<title>Mr. Torvo Premium Beard Balm Label</title>
<link rel="stylesheet" href="https://fonts.googleapis.com/css2?family=Cinzel:wght@400;600&family=Lobster&family=Roboto:ital,wght@0,300;0,400;1,300;1,500&display=swap">
<style>
  :root {
    --backdrop: #807f80;
    --label-black: #0d0d0d;
    --label-black-soft: #1c1c1c;
    --silver-light: #f2f2f2;
    --silver: #c8c8c8;
    --silver-dark: #8e8e8e;
    --text-silver: #d2d2d2;
    --text-muted: #a9a9a9;
  }
  * { box-sizing: border-box; margin: 0; padding: 0; }
  html, body {
    width: 1200px; height: 1200px; overflow: hidden;
    background: var(--backdrop);
  }
  .canvas {
    position: relative; width: 1200px; height: 1200px;
    background: radial-gradient(ellipse at 50% 45%, #8a898a 0%, var(--backdrop) 70%);
  }
  .label {
    position: absolute; left: 60px; top: 470px;
    width: 1080px; height: 260px;
    background: linear-gradient(180deg, var(--label-black-soft), var(--label-black) 50%, var(--label-black-soft));
    display: grid; grid-template-columns: 1fr 1fr 1fr;
    box-shadow: 0 18px 30px rgba(0,0,0,0.35);
  }
  .band {
    position: absolute; left: 0; right: 0; height: 14px;
    background: linear-gradient(180deg, var(--silver-dark), var(--silver-light) 45%, var(--silver) 60%, var(--silver-dark));
  }
  .band--top { top: 14px; }
  .band--bottom { bottom: 14px; }
  .panel {
    position: relative; padding: 44px 40px;
    display: flex; flex-direction: column; justify-content: center;
  }
  .panel + .panel { border-left: 1px solid #262626; }
  .features {
    list-style: none; font-family: "Roboto", sans-serif; font-weight: 300;
    font-size: 18px; line-height: 1.45; color: var(--text-silver);
  }
  .features li { position: relative; padding-left: 22px; }
  .features li::before {
    content: "★"; position: absolute; left: 0; top: 1px;
    font-size: 11px; color: var(--silver);
  }
  .panel--front { align-items: center; text-align: center; padding: 40px 20px 34px; }
  .emblem {
    width: 74px; height: 92px; border-radius: 36px 36px 6px 6px;
    background: linear-gradient(160deg, var(--silver-light), var(--silver-dark));
  }
  .brand-name {
    margin-top: 6px; font-family: "Lobster", cursive;
    font-size: 26px; color: var(--text-muted); line-height: 1.1;
  }
  .product-tier {
    margin-top: 4px; font-family: "Cinzel", serif; font-size: 16px;
    letter-spacing: 6px; color: var(--text-silver);
  }
  .product-tier .star { font-size: 9px; letter-spacing: 0; vertical-align: 3px; margin: 0 4px; }
  .product-name {
    font-family: "Cinzel", serif; font-weight: 600; font-size: 28px;
    letter-spacing: 1px; color: var(--silver-light); line-height: 1.1;
  }
  .ingredients {
    font-family: "Roboto", sans-serif; font-weight: 300; font-size: 16px;
    line-height: 1.4; color: var(--text-muted);
  }
  .ingredients em { font-weight: 500; color: var(--text-silver); }
  .net-weight {
    margin-top: 12px; font-family: "Roboto", sans-serif; font-size: 24px;
    font-weight: 300; color: var(--silver-light);
  }
  .net-weight .batch { font-style: italic; font-weight: 500; font-size: 18px; }
</style>
</head>
<body>
<main class="canvas">
  <section class="label" aria-label="Mr. Torvo Premium Beard Balm label">
    <div class="band band--top"></div>
    <div class="band band--bottom"></div>

    <div class="panel panel--features">
      <ul class="features">
        <li>All Natural Oils</li>
        <li>Fresh Cucumber and Black Licorice (Flavor of the balm)</li>
        <li>Aphrodisiac Scent</li>
      </ul>
    </div>

    <div class="panel panel--front">
      <div class="emblem" role="img" aria-label="Silver emblem of a bearded man in a suit and tie"></div>
      <p class="brand-name">Mr. Torvo</p>
      <p class="product-tier"><span class="star">★</span>PREMIUM<span class="star">★</span></p>
      <h1 class="product-name">BEARD BALM</h1>
    </div>

    <div class="panel panel--details">
      <p class="ingredients"><em>Ingredients:</em> Coconut Oil, Shea Butter, Cocoa Butter, Oil Jojoba, Oil Sweet Almond Oil, Lanolin, Argan Oil, Rosehip Oil, and Essential oils</p>
      <p class="net-weight">2 OZ <span class="batch">/ BATCH: 014</span></p>
    </div>
  </section>
</main>
</body>
</html>
```